Meditations CD Cover
Zielgruppe
Wir unterstützen Therapeuten ihre Praxis aufzubauen.
Aufgabenstellung
Ich wünsche einen CD Cover mit Rückseite und CD Druck, wo nicht zu esoterisch aussieht. Bitte keine Buddha, Steine, Yoga, Lotusblume!
ich hätte gerne mein Bild im Vordergrund, nicht zu prominent, klar strukturiert und nicht zu schwer, lieber mehr Platz lassen.
ich hätte gerne eine CD Jewel Cases.
Bitte eine ganz neutralle CD ohne das Grün von der Website. (licht-weg-studio.ch)
Die Meditation ist eine Mischung zwischen Business und Meditation, es geht um Kundenfindung.
Etwas schlichtes und modernes.
Was rauf muss:
CD Cover
Doria Pfannstiel-Kuhmer
Mein Foto
Titel:
Finde Deinen Auftrag, Pfad des Einklangs!
bitte auch schreiben: die ÜBUNGS-CD zum Buch
Logo und mein Bild, nicht zu prominent!!!!
Beispiel: http://marenbextolli.com/
http://www.bildquellhaus.com/vector/electric-bulb-48201937?st=7302846
http://www.bildquellhaus.com/vector/dart-board-48202541?st=913ab27
http://wolkenklang-audio.com/hagen-lutz-deine-reise-zu-glanz-reichtum-und-freude-cd
Rückseite:
mein Foto und der Text:
Gehen Sie in die Resonanz und finden Sie den richtigen Klienten.
Gerne unterstütze ich Sie auf diesem wundervollen Weg ...
Mein Name ist Doria Pfannstiel, ich bin erfolgreiche Unternehmerin, die zugleich spiri- tuell denkt und handelt. Und ich bin fest davon überzeugt. Es gibt eine innere Kraft, die nicht nur Berge versetzt. Sondern auch Ihre Praxis fullt.
Auf dieser CD werden Sie angeleitet sich mit ihrem Idealkunden zu treffen. Sie werden entdecken welche Probleme oder Herausforderungen, Wünsche und Ziele Ihr potenzieller Klient.
Vielen Dank und viel Spass :-)

```html
<!DOCTYPE html>
<html lang="de">
<head>
<meta charset="utf-8">
<title>Übungs-CD – Cover und Rückseite</title>
<link rel="stylesheet" href="https://fonts.googleapis.com/css2?family=Didact+Gothic&family=Open+Sans:wght@700&family=Dancing+Script:wght@400&display=swap">
<style>
  :root {
    --paper: #ffffff;
    --band: #fcd886;
    --body-text: #8d93a8;
    --title-text: #55565f;
    --portrait-hair: #4b4a58;
    --portrait-skin: #d9c9a6;
    --portrait-blouse: #f3ead2;
    --shadow: rgba(0,0,0,0.28);
  }
  * { margin: 0; padding: 0; box-sizing: border-box; }
  html, body { width: 1200px; height: 520px; overflow: hidden; background: var(--paper); }
  .canvas { position: relative; width: 1200px; height: 520px; }

  .panel { position: absolute; top: 0; height: 480px; box-shadow: 3px 3px 5px var(--shadow); overflow: hidden; }
  .back { left: 44px; width: 623px; }
  .front { left: 694px; width: 480px; }

  .photo { position: absolute; left: 0; width: 100%; }
  .back .photo-sky { top: 0; height: 95px;
    background: linear-gradient(100deg, #a88a4c 0%, #e6c170 30%, #b9a068 60%, #6f7d6a 100%); }
  .back .photo-road { top: 385px; height: 95px;
    background: linear-gradient(180deg, #8f9c86 0%, #5f7a77 45%, #6b8380 100%); }

  .band { position: absolute; left: 0; width: 100%; background: var(--band); }
  .back .band { top: 95px; height: 290px; }

  .spine { position: absolute; font-family: 'Didact Gothic', sans-serif; font-weight: 700;
    font-size: 11.5px; line-height: 14px; color: var(--body-text); white-space: nowrap; }
  .spine-left { left: 16px; top: 302px; transform: rotate(-90deg); transform-origin: 0 0; }
  .spine-right { left: 610px; top: 178px; transform: rotate(90deg); transform-origin: 0 0; }

  .portrait { position: absolute; left: 396px; top: 193px; width: 196px; height: 192px; z-index: 1; }

  .letter { position: absolute; left: 68px; top: 111px; z-index: 2;
    font-family: 'Didact Gothic', sans-serif; font-size: 13.4px; line-height: 14.4px;
    color: var(--body-text); white-space: nowrap; }
  .letter p { margin-bottom: 14.4px; }
  .signature { font-family: 'Dancing Script', cursive; font-size: 17px; line-height: 20px; color: var(--body-text); margin-top: -2px; }

  .brand { display: flex; align-items: center; gap: 6px; }
  .brand-dot { width: 30px; height: 30px; border-radius: 50%; background: #e9a66a; }
  .brand-name { font-family: 'Didact Gothic', sans-serif; font-size: 23px; color: var(--title-text); line-height: 1; }
  .back .brand { position: absolute; left: 68px; top: 337px; z-index: 2; }

  .front .photo-top { top: 0; height: 18px; background: linear-gradient(90deg, #3d5d67 0%, #6f8a80 50%, #e8dca8 100%); }
  .front .band-top { top: 18px; height: 137px; }
  .front .photo-walk { top: 155px; height: 274px;
    background: linear-gradient(160deg, #3f6475 0%, #5c7f86 35%, #b99c62 60%, #4e6766 85%, #3d5050 100%); }
  .front .band-bottom { top: 429px; height: 51px; }

  .title { position: absolute; top: 37px; left: 0; width: 100%; text-align: center;
    font-family: 'Dancing Script', cursive; font-weight: 400; font-size: 38px; line-height: 32px; color: var(--title-text); }
  .author { position: absolute; top: 107px; left: 0; width: 100%; text-align: center;
    font-family: 'Dancing Script', cursive; font-size: 22px; line-height: 28px; color: var(--title-text); }

  .front .brand { position: absolute; left: 50px; top: 436px; }
  .front .brand-dot { width: 36px; height: 36px; }
  .front .brand-name { font-size: 26px; }
  .tagline { position: absolute; left: 194px; top: 438px; font-family: 'Open Sans', sans-serif; font-weight: 700;
    font-size: 19.5px; line-height: 26px; color: var(--title-text); white-space: nowrap; }
</style>
</head>
<body>
<div class="canvas">

  <section class="panel back">
    <div class="photo photo-sky" role="img" aria-label="Unscharfer Waldweg im warmen Gegenlicht"></div>
    <div class="band"></div>
    <div class="photo photo-road" role="img" aria-label="Asphaltstrasse in geringer Schärfentiefe"></div>

    <div class="spine spine-left">Doria Pfannstiel-Kuhmer</div>
    <div class="spine spine-right">Doria Pfannstiel-Kuhmer</div>

    <svg class="portrait" viewBox="0 0 196 192" role="img" aria-label="Porträtfoto der Autorin in weisser Bluse">
      <path d="M0 192 C20 150 55 130 80 118 L130 118 C160 130 185 150 196 192 Z" fill="var(--portrait-blouse)"/>
      <ellipse cx="100" cy="52" rx="48" ry="52" fill="var(--portrait-hair)"/>
      <ellipse cx="104" cy="70" rx="38" ry="46" fill="var(--portrait-skin)"/>
    </svg>

    <div class="letter">
      <p>Gehen Sie in die Resonanz und finden Sie den richtigen Klienten.<br>Gerne unterstütze ich Sie auf diesem wundervollen Weg.</p>
      <p>Mein Name ist Doria Pfannstiel, ich bin erfolgreiche Unternehmerin,<br>die zugleich spirituell denkt und handelt. Und ich bin fest davon<br>überzeugt. Es gibt eine innere Kraft, die nicht nur Berge versetzt.<br>Sondern auch Ihre Praxis füllt.</p>
      <p>Auf dieser CD werden Sie angeleitet sich mit ihrem Idealkunden<br>zu treffen. Sie werden entdecken welche Probleme oder Heraus-<br>forderungen, Wünsche und Ziele Ihr potenzieller Klient.</p>
      <p>Vielen Dank und viel Spass</p>
      <div class="signature">Doria Pfannstiel-Kuhmer</div>
    </div>

    <div class="brand">
      <span class="brand-dot"></span>
      <span class="brand-name">DPK</span>
    </div>
  </section>

  <section class="panel front">
    <div class="photo photo-top" role="img" aria-label="Ausschnitt der Wegszene"></div>
    <div class="band band-top"></div>
    <h1 class="title">Finde Deinen Auftrag,<br>Pfad des Einklangs!</h1>
    <div class="author">Doria Pfannstiel-Kuhmer</div>
    <div class="photo photo-walk" role="img" aria-label="Füsse in Jeans und Stoffschuhen gehen auf einer Strasse im Herbstwald"></div>
    <div class="band band-bottom"></div>
    <div class="brand">
      <span class="brand-dot"></span>
      <span class="brand-name">DPK</span>
    </div>
    <div class="tagline">die ÜBUNGS-CD zum Buch</div>
  </section>

</div>
</body>
</html>
```